Torvale Works- Plumbing Business Card

We need a business card design for a new company that services Canberra and surrounds. We are a professional family-owned plumbing company who has 20+ years' experience. We would like to use our logo as well as the colours black, white, grey and the signature green. The final design needs to communicate professional, high-end, plumbing with reliable service. We provide obligation free quotes and are open 24/7. Services include: Bathroom/kitchen renovations, drainage, stormwater, water leaks, plumbing maintenance, water tanks and septics.

Target Market(s)

Homeowners, real estate agents, builders, small business owners

Industry/Entity Type

Plumbing & Construction

Font styles to use
Serif
Sans Serif

Colors
59FF00
82FF00
B8FF75
E3FFCB
F4FFEA

Requirements
Must have
• Must have logo, example of services and contact details

```html
<!DOCTYPE html>
<html lang="en">
<head>
<meta charset="utf-8">
<title>Torvale Works – Business Card</title>
<link rel="stylesheet" href="https://fonts.googleapis.com/css2?family=Poppins:wght@700&family=Roboto:wght@400;700;900&display=swap">
<style>
  :root {
    --green: #17a54c;
    --black: #0b0d0c;
    --ink: #3a3a3a;
    --white: #ffffff;
    --page: #ffffff;
  }
  * { box-sizing: border-box; margin: 0; padding: 0; }
  html, body {
    width: 1009px; height: 1200px; overflow: hidden;
    background: var(--page);
    font-family: "Roboto", Arial, sans-serif;
    color: var(--ink);
  }
  .card {
    position: absolute; left: 122px; width: 801px; height: 458px;
    background: var(--white); overflow: hidden;
    box-shadow: 0 0 0 1px #ececec;
  }
  .card--front { top: 87px; }
  .card--back { top: 602px; }

  /* front */
  .front-shapes { position: absolute; inset: 0; }
  .holder-name {
    position: absolute; left: 53px; top: 118px;
    font-family: "Poppins", Arial, sans-serif; font-weight: 700;
    font-size: 49px; line-height: 1; letter-spacing: 0.5px; color: #383838;
  }
  .name-rule {
    position: absolute; left: 53px; top: 182px; width: 360px; height: 3px;
    background: var(--green);
  }
  .contact-list { position: absolute; left: 49px; top: 259px; list-style: none; }
  .contact-item {
    display: flex; align-items: center; height: 44px;
    font-size: 25px; color: var(--ink);
  }
  .contact-icon { width: 29px; height: 29px; margin-right: 19px; flex: none; }
  .wordmark {
    position: absolute; color: var(--white); font-weight: 900;
    text-transform: uppercase; text-align: center; line-height: 1;
  }
  .wordmark--front { left: 560px; top: 340px; width: 200px; font-size: 34px; }

  /* back */
  .back-panel {
    position: absolute; left: 0; top: 0; width: 100%; height: 258px;
    background: var(--green);
  }
  .wordmark--back { left: 0; top: 74px; width: 100%; font-size: 58px; }
  .service-rule {
    position: absolute; left: 0; top: 285px; width: 100%; height: 5px;
    background: var(--green);
  }
  .service-badge { position: absolute; left: 298px; top: 271px; width: 201px; height: 32px; }
  .service-badge-label {
    position: absolute; left: 298px; top: 271px; width: 201px; height: 32px;
    display: flex; align-items: center; justify-content: center;
    color: var(--white); font-weight: 700; font-size: 19px; letter-spacing: 0.5px;
  }
  .service-list { position: absolute; top: 316px; list-style: none; }
  .service-list--left { left: 44px; }
  .service-list--right { left: 465px; }
  .service-item {
    display: flex; align-items: center; height: 36px;
    font-size: 23.5px; color: #2a2a2a;
  }
  .service-item::before {
    content: ""; width: 9px; height: 9px; border-radius: 50%;
    background: #111; margin-right: 10px; flex: none;
  }
  .base-band {
    position: absolute; left: 0; bottom: 0; width: 100%; height: 17px;
    background: var(--black);
  }
</style>
</head>
<body>

<section class="card card--front">
  <svg class="front-shapes" viewBox="0 0 801 458" width="801" height="458" aria-hidden="true">
    <polygon fill="var(--black)" points="668,0 687,0 464,349 516,458 499,458 446,349"/>
    <polygon fill="var(--green)" points="709,0 801,0 801,458 538,458 484,349"/>
  </svg>

  <h1 class="holder-name">CALDER VOSS</h1>
  <div class="name-rule"></div>

  <ul class="contact-list">
    <li class="contact-item">
      <svg class="contact-icon" viewBox="0 0 30 30" aria-hidden="true">
        <circle cx="15" cy="15" r="15" fill="var(--green)"/>
        <path d="M15 7a5.5 5.5 0 0 0-5.5 5.5c0 4 5.5 10 5.5 10s5.5-6 5.5-10A5.5 5.5 0 0 0 15 7z" fill="#fff"/>
        <circle cx="15" cy="12.5" r="2.2" fill="var(--green)"/>
      </svg>
      Torvale Plumbing Canberra
    </li>
    <li class="contact-item">
      <svg class="contact-icon" viewBox="0 0 30 30" aria-hidden="true">
        <circle cx="15" cy="15" r="15" fill="var(--green)"/>
        <path d="M10.5 8.5l2.5-.5 1.5 3.5-1.8 1.3a8 8 0 0 0 4.5 4.5l1.3-1.8 3.5 1.5-.5 2.5c-.3 1-1.3 1.6-2.3 1.4A12 12 0 0 1 9.1 10.8c-.2-1 .4-2 1.4-2.3z" fill="#fff"/>
        <path d="M17 8.5a5 5 0 0 1 4.5 4.5M17 11a2.5 2.5 0 0 1 2 2" stroke="#fff" stroke-width="1.4" fill="none" stroke-linecap="round"/>
      </svg>
      0400 123 987
    </li>
    <li class="contact-item">
      <svg class="contact-icon" viewBox="0 0 30 30" aria-hidden="true">
        <circle cx="15" cy="15" r="15" fill="var(--green)"/>
        <rect x="8" y="10" width="14" height="10" rx="1.5" fill="#fff"/>
        <path d="M8.5 10.8L15 15.5l6.5-4.7" stroke="var(--green)" stroke-width="1.4" fill="none"/>
      </svg>
      info@torvaleworks.com
    </li>
    <li class="contact-item">
      <svg class="contact-icon" viewBox="0 0 30 30" aria-hidden="true">
        <circle cx="15" cy="15" r="15" fill="var(--green)"/>
        <g stroke="#fff" stroke-width="1.2" fill="none">
          <circle cx="15" cy="15" r="6.5"/>
          <ellipse cx="15" cy="15" rx="2.8" ry="6.5"/>
          <path d="M8.5 15h13M9.5 11.5h11M9.5 18.5h11"/>
        </g>
      </svg>
      torvaleworks.com.au
    </li>
  </ul>

  <p class="wordmark wordmark--front">Torvale<br>Works</p>
</section>

<section class="card card--back">
  <div class="back-panel"></div>
  <p class="wordmark wordmark--back">Torvale<br>Works</p>

  <div class="service-rule"></div>
  <svg class="service-badge" viewBox="0 0 201 32" aria-hidden="true">
    <polygon fill="var(--green)" points="14,0 187,0 201,16 187,32 14,32 0,16"/>
  </svg>
  <p class="service-badge-label">24/7 SERVICES</p>

  <ul class="service-list service-list--left">
    <li class="service-item">Bathroom/Kitchen Renovations</li>
    <li class="service-item">Drainage</li>
    <li class="service-item">Plumbing Maintenance</li>
  </ul>
  <ul class="service-list service-list--right">
    <li class="service-item">Stormwater</li>
    <li class="service-item">Water Leaks</li>
    <li class="service-item">Water Tanks and Septics</li>
  </ul>

  <div class="base-band"></div>
</section>

</body>
</html>
```